Tarvolink - Smart Border Flow Reshaping Trade

Web Design for international start-up, which is automating customs clearance processes for forwarding companies by applying a web application, which is operating with artificial intelligence and robotic process automation. Tarvolink pursues the vision of supporting forwarding companies successfully in becoming digital masters and co-creates innovative software solutions with all participants (ex- and importers of goods) along value-added chains. With intelligent/smart/digital customs clearance software or in other words, a virtual customs clearance roboter tailord to the customers needs, we are transforming businesses. The website could look like this:

https://www.qorvanta.example/uk-en/index.php
or
https://pagelumen.example/theme/brindlemoor

Please use colours and designs you think would be the best fit. These websites are just here to give you an idea of how the webdesign could look like. Use the attached logo design as a basis for further web design. You can use the provided pictures, but you can also use your own ones, if you think they are better suited. But please take care, that they have a high resolution quality.

Description of Website: The website is transparent and modern. It provides seven pages such as homepage, products, web app, the about us, working at Tarvolink, News, contact us and search results page. The homepage or landing page should be filled with a short description of the company, what Tarvolink is doing, how they will support its customers and will also include a video of the provided solution. Products provide obviously information about different products and their characteristics. Web app page includes information about principles and technologies that get the software going. The about us page includes unique advantages and value propositions for customers and the contact us, as the name already says, will provide contact information and possibilities to contact us. The rest is also obvious (for additional information look up the website of QVT, priorly provided link - the page is also available in english).

If you have any questions, I am happy to answer them any time.
Updates

I have to think about the text that I want to have included into the design and hadn't have the time to compose it.

Target Market(s)

Forwarding Companies, Ex-/Importers

Industry/Entity Type

It Company

Number of Pages Required

5+ page

Requirements
Must have
• The web design should be designes according to the attached logo of Tarvolink.

```html
<!DOCTYPE html>
<html lang="en">
<head>
<meta charset="utf-8">
<title>Tarvolink – Smart Border Flow Reshaping Trade</title>
<link rel="stylesheet" href="https://fonts.googleapis.com/css2?family=Montserrat:wght@300;400;600;700&family=Open+Sans:wght@400;600&display=swap">
<style>
:root{
  --teal:#1c6f99;
  --teal-dark:#15597d;
  --teal-light:#2b8cbd;
  --ink:#1e1e22;
  --charcoal:#2a2b30;
  --grey-bg:#e9e9eb;
  --text:#4a4a4f;
  --muted:#8a8a90;
  --white:#ffffff;
  --pink:#d8407a;
  --violet:#5a3d8c;
}
*{box-sizing:border-box;margin:0;padding:0}
html,body{width:1200px;height:5255px;overflow:hidden}
body{font-family:"Open Sans",Arial,sans-serif;color:var(--text);background:var(--white);position:relative}
h1,h2,h3,h4,.nav,.btn{font-family:"Montserrat",Arial,sans-serif}
section,header,footer{position:absolute;left:0;width:1200px}
.photo{position:absolute}

/* header / hero */
.hero{top:0;height:672px;overflow:hidden}
.hero .photo{inset:0;background:linear-gradient(115deg,#3a2a6e 0%,var(--pink) 38%,#b03a86 55%,#2a5fa8 80%,#1b2f63 100%)}
.hero::after{content:"";position:absolute;inset:0;background:rgba(20,20,40,.25)}
.nav{position:absolute;top:0;left:0;width:1200px;height:80px;background:rgba(20,20,30,.55);z-index:2;display:flex;align-items:center;padding:0 60px}
.brand{font-family:"Montserrat",sans-serif;font-weight:600;font-size:30px;color:var(--white);letter-spacing:1px;display:flex;align-items:center;gap:10px}
.brand .dot{width:12px;height:12px;border-radius:50%;background:var(--teal-light)}
.nav ul{list-style:none;display:flex;gap:34px;margin-left:auto;font-size:15px;color:var(--white);font-weight:400}
.hero-title{position:absolute;top:350px;width:100%;text-align:center;z-index:2;color:var(--white);font-weight:600;font-size:50px;line-height:1.2;letter-spacing:2px;text-transform:uppercase}
.play{position:absolute;top:515px;left:570px;z-index:2}

/* about */
.about{top:672px;height:548px;background:var(--teal);color:var(--white);text-align:center}
.about h2{margin-top:50px;font-size:34px;font-weight:600;letter-spacing:3px}
.rule{width:60px;height:2px;background:var(--white);margin:14px auto 0}
.about .lead{margin:40px auto 0;width:900px;font-family:"Montserrat",sans-serif;font-weight:600;font-size:19px;line-height:1.4;text-transform:uppercase;letter-spacing:.5px}
.features{display:flex;justify-content:center;gap:60px;margin-top:50px}
.feature{width:200px}
.feature .ico{width:84px;height:84px;border-radius:50%;background:var(--teal-light);margin:0 auto;display:flex;align-items:center;justify-content:center}
.feature h4{margin-top:18px;font-size:14px;font-weight:600;letter-spacing:1px;text-transform:uppercase}
.feature p{margin-top:10px;font-size:12px;line-height:1.5;opacity:.85}

/* products */
.products{top:1220px;height:753px}
.prod-row{position:absolute;left:0;width:1200px;height:376px;display:flex}
.prod-text{width:600px;padding:50px 60px}
.prod-text .meta{font-size:12px;letter-spacing:1px;text-transform:uppercase}
.prod-text h3{margin-top:8px;font-size:22px;font-weight:600;letter-spacing:1px}
.prod-text p{margin-top:18px;font-size:13px;line-height:1.7}
.dark{background:var(--ink);color:#d8d8dc}
.dark h3{color:var(--white)}
.light{background:var(--white);color:var(--text)}
.light h3{color:var(--ink)}
.products .label{position:absolute;top:20px;left:520px;z-index:3;font-family:"Montserrat",sans-serif;font-size:36px;color:var(--white)}
.ph-desk{background:linear-gradient(135deg,#9aa4ad,#5d666f 60%,#3b4147)}
.ph-laptop{background:linear-gradient(135deg,#c9d3dc,#3f6f9c 55%,#1e3a5f)}

/* news */
.news{top:1973px;height:762px;background:linear-gradient(180deg,#ffffff,#f2f4f6);text-align:center}
.news h2{margin-top:70px;font-size:28px;font-weight:600;letter-spacing:3px;color:var(--ink)}
.news .sub{margin-top:40px;font-size:24px;color:var(--text)}
.cards{position:absolute;top:290px;left:160px;display:flex;gap:20px}
.card{width:205px;text-align:left}
.card .photo{position:relative;height:220px}
.card .meta{margin-top:18px;font-size:11px;text-transform:uppercase;color:var(--ink)}
.card p{margin-top:10px;font-size:12px;line-height:1.6;color:var(--muted)}

/* band */
.band{top:2735px;height:247px;background:var(--teal);color:var(--white);display:flex;padding:75px 160px;gap:80px}
.band .col{display:flex;gap:22px;width:420px}
.band p{font-size:13px;line-height:1.6}

/* web app */
.webapp{top:2982px;height:583px;overflow:hidden}
.webapp .bg{inset:0;background:linear-gradient(120deg,#2c2d31,#1a1b1e 60%,#303236)}
.webapp .inner{position:absolute;left:160px;top:110px;width:440px;color:#d8d8dc}
.webapp h3{font-size:22px;font-weight:600;color:var(--white);letter-spacing:1px}
.webapp p{margin-top:20px;font-size:13px;line-height:1.7}
.btn{display:block;width:300px;height:34px;margin-top:14px;background:var(--teal);color:var(--white);font-size:12px;font-weight:600;letter-spacing:1px;text-transform:uppercase;line-height:34px;padding-left:20px}
.btn:first-of-type{margin-top:30px}
.phone{left:720px;top:55px;width:240px;height:470px;border-radius:30px;background:linear-gradient(160deg,#f4f4f6,#cfd3d8 70%,#9aa8b6)}

/* team */
.team{top:3565px;height:717px;background:var(--grey-bg);text-align:center}
.team h2{margin-top:90px;font-size:28px;font-weight:600;letter-spacing:3px;color:var(--ink)}
.team .sub{margin-top:35px;font-size:21px;color:var(--text)}
.members{position:absolute;top:250px;left:160px;display:flex;gap:25px}
.member{width:200px}
.member .photo{position:relative;height:290px;background:linear-gradient(170deg,#d9d9db,#6c6c70 70%,#2c2c30)}
.member .tag{background:var(--white);padding:14px 0;box-shadow:0 2px 6px rgba(0,0,0,.1)}
.member h4{font-size:14px;font-weight:600;color:var(--teal);text-transform:uppercase}
.member span{font-size:11px;color:var(--muted)}

/* contact */
.contact{top:4282px;height:650px;overflow:hidden;text-align:center}
.contact .bg{inset:0;background:linear-gradient(180deg,#27292e,#1a1b1f)}
.contact .content{position:absolute;inset:0}
.contact .brand{justify-content:center;margin-top:80px;font-size:64px;font-weight:600}
.contact h2{margin-top:26px;font-size:30px;font-weight:700;color:var(--white);letter-spacing:1px}
.fields{position:absolute;top:290px;left:160px;width:880px}
.row{display:flex;gap:20px}
.field{flex:1;height:42px;background:var(--white);text-align:left;padding:10px 14px;font-size:13px;color:var(--text)}
.field.msg{height:110px;margin-top:20px;flex:none;width:880px}
.submit{display:inline-block;margin-top:24px;width:160px;height:40px;background:var(--teal);color:var(--white);font-family:"Montserrat",sans-serif;font-weight:600;font-size:14px;line-height:40px;letter-spacing:1px}

/* map + footer */
.map{top:4932px;height:268px;background:linear-gradient(135deg,#2b3340,#1c2430 60%,#26313f)}
footer{top:5200px;height:55px;background:#141518;color:#9a9aa0;font-size:12px;padding:20px 60px}
</style>
</head>
<body>

<header class="hero">
  <div class="photo" role="img" aria-label="Close-up photo of a tech device in pink and blue stage light"></div>
  <nav class="nav">
    <div class="brand">Tarvolink</div>
    <ul>
      <li>Home</li><li>About Us</li><li>Products</li><li>Web app</li><li>Working at Tarvolink</li><li>News</li><li>Contact us</li>
    </ul>
  </nav>
  <h1 class="hero-title">Smart Border Flow<br>Reshaping Trade</h1>
  <svg class="play" width="60" height="60" viewBox="0 0 60 60"><circle cx="30" cy="30" r="27" fill="none" stroke="#fff" stroke-width="2"/><path d="M24 18 L42 30 L24 42Z" fill="#fff"/></svg>
</header>

<section class="about">
  <h2>ABOUT US</h2>
  <div class="rule"></div>
  <p class="lead">Automating customs clearance processes for forwarding companies by applying a web application, which is operating with artificial intelligence and robotic process automation</p>
  <div class="features">
    <div class="feature"><div class="ico"><svg width="34" height="34" viewBox="0 0 24 24" fill="none" stroke="#fff" stroke-width="1.8"><rect x="3" y="3" width="18" height="18"/><path d="M8 16l8-8M14 8h2v2"/></svg></div><h4>Fast Clearance</h4><p>Filing runs in minutes, not days, with smart checks on every entry.</p></div>
    <div class="feature"><div class="ico"><svg width="34" height="34" viewBox="0 0 24 24" fill="none" stroke="#fff" stroke-width="1.8"><rect x="3" y="3" width="18" height="18"/><path d="M8 16l8-8M14 8h2v2"/></svg></div><h4>Smart Robots</h4><p>Virtual agents learn each client flow and handle routine tasks.</p></div>
    <div class="feature"><div class="ico"><svg width="34" height="34" viewBox="0 0 24 24" fill="none" stroke="#fff" stroke-width="1.8"><rect x="3" y="3" width="18" height="18"/><path d="M8 16l8-8M14 8h2v2"/></svg></div><h4>Open Network</h4><p>Exporters and importers share one clear view of each shipment.</p></div>
    <div class="feature"><div class="ico"><svg width="34" height="34" viewBox="0 0 24 24" fill="none" stroke="#fff" stroke-width="1.8"><circle cx="11" cy="11" r="6"/><path d="M16 16l5 5"/></svg></div><h4>Digital Masters</h4><p>We guide forwarders step by step into a fully digital routine.</p></div>
  </div>
</section>

<section class="products">
  <div class="label">Products</div>
  <div class="prod-row" style="top:0">
    <div class="prod-text dark">
      <div class="meta">Jan 2024 | Product</div>
      <h3>AKITA INU DOG</h3>
      <p>Our clearance robot reads invoices, sorts tariff codes and prepares each declaration with no manual typing. Teams save hours every day and cut errors at the border.</p>
      <p>Every step is logged, so you always know where a file stands and why.</p>
    </div>
    <div class="photo ph-desk" style="position:relative;width:600px" role="img" aria-label="Top-down photo of a desk with keyboard, tablet and product brochure"></div>
  </div>
  <div class="prod-row" style="top:376px">
    <div class="photo ph-laptop" style="position:relative;width:600px" role="img" aria-label="Photo of hands typing on a laptop showing the product screen"></div>
    <div class="prod-text light">
      <div class="meta">Jan 2024 | Product</div>
      <h3>AKITA INU DOG</h3>
      <p>The web app links your team with clients and partners along the value chain. Upload papers once and let the system fill forms, track status and send alerts.</p>
      <p>Built for forwarders of every size, ready to scale with you.</p>
    </div>
  </div>
</section>

<section class="news">
  <h2>NEWS</h2>
  <p class="sub">We love clean design and advanced digital solutions</p>
  <div class="cards">
    <article class="card"><div class="photo" style="background:linear-gradient(150deg,#7f8c99,#3d4a57)" role="img" aria-label="News photo of a meeting room"></div><div class="meta">Mar 2024 | News</div><p>New release brings faster tariff lookup and a cleaner dashboard for all users.</p></article>
    <article class="card"><div class="photo" style="background:linear-gradient(150deg,#c3ccd4,#6f7f8e)" role="img" aria-label="News photo of a team at work"></div><div class="meta">Mar 2024 | News</div><p>We joined a trade forum to share how robots change customs work today.</p></article>
    <article class="card"><div class="photo" style="background:linear-gradient(150deg,#a9b9c9,#3f6f9c)" role="img" aria-label="News photo of a laptop and documents"></div><div class="meta">Feb 2024 | News</div><p>Partners in three new ports can now file directly through the app.</p></article>
    <article class="card"><div class="photo" style="background:linear-gradient(150deg,#8d96a0,#2f3a46)" role="img" aria-label="News photo of a workspace"></div><div class="meta">Feb 2024 | News</div><p>Our team grows: meet the new people shaping smart border flow.</p></article>
  </div>
</section>

<section class="band">
  <div class="col">
    <svg width="44" height="44" viewBox="0 0 24 24" fill="none" stroke="#fff" stroke-width="1.8"><path d="M3 21h6l11-11-6-6L3 15z"/><path d="M3 21h18"/></svg>
    <p>Fewer manual steps mean fewer delays. Our clients clear goods faster and focus on growing trade relations instead of paperwork.</p>
  </div>
  <div class="col">
    <svg width="44" height="44" viewBox="0 0 24 24" fill="none" stroke="#fff" stroke-width="1.8"><path d="M3 21h6l11-11-6-6L3 15z"/><path d="M3 21h18"/></svg>
    <p>We co-create software with all partners along the chain, so each tool fits real needs and works from the first day on.</p>
  </div>
</section>

<section class="webapp">
  <div class="photo bg" role="img" aria-label="Dark background photo of a desk with devices"></div>
  <div class="inner">
    <h3>WEB APP</h3>
    <p>Artificial intelligence and robotic process automation drive every part of the app. It learns from each case, checks data on the fly and keeps your declarations compliant.</p>
    <span class="btn">Smart Robot Process</span>
    <span class="btn">Open Interfaces</span>
    <span class="btn">Customs Ready Output</span>
  </div>
  <div class="photo phone" role="img" aria-label="Smartphone showing the web app home screen"></div>
</section>

<section class="team">
  <h2>OUR TEAM</h2>
  <p class="sub">People who make smart border flow happen</p>
  <div class="members">
    <div class="member"><div class="photo" role="img" aria-label="Portrait photo of a team member"></div><div class="tag"><h4>Oren Halvik</h4><span>CEO</span></div></div>
    <div class="member"><div class="photo" role="img" aria-label="Portrait photo of a team member"></div><div class="tag"><h4>Mira Castell</h4><span>CTO</span></div></div>
    <div class="member"><div class="photo" role="img" aria-label="Portrait photo of a team member"></div><div class="tag"><h4>Dario Venn</h4><span>Developer</span></div></div>
    <div class="member"><div class="photo" role="img" aria-label="Portrait photo of a team member"></div><div class="tag"><h4>Lena Kroft</h4><span>Designer</span></div></div>
  </div>
</section>

<section class="contact">
  <div class="photo bg" role="img" aria-label="Dark photo of an office background"></div>
  <div class="content">
    <div class="brand">Tarvolink</div>
    <h2>WE'D LOVE TO HEAR ABOUT YOUR PROJECT.</h2>
    <div class="fields">
      <div class="row"><div class="field">Name</div><div class="field">Email</div><div class="field">Phone</div></div>
      <div class="field msg">Message</div>
      <span class="submit">SUBMIT</span>
    </div>
  </div>
</section>

<section class="map" role="img" aria-label="Dark street map showing the office location"></section>

<footer>© 2024 Tarvolink. All rights reserved.</footer>

</body>
</html>
```